'Tarvel' a financial/crypto-currency exchange in the middle east

On the card we need 1) Name 2) title 3) email address 4) phone number using the same colors and theme as the logo. On one side we just want the logo and we want the whole card to be in blue (same blue as logo) with the logo in the back being white.
Industry/Entity Type
Financial

```html
<!DOCTYPE html>
<html lang="en">
<head>
<meta charset="utf-8">
<title>Tarvel Business Card</title>
<link href="https://fonts.googleapis.com/css2?family=Montserrat:wght@400;500;700;800&display=swap" rel="stylesheet">
<style>
  :root {
    --brand-blue: #0b93cf;
    --brand-blue-soft: #2aa3d8;
    --card-white: #ffffff;
    --tint: #e6eef8;
    --stage: #2a2a2a;
  }
  * { margin: 0; padding: 0; box-sizing: border-box; }
  html, body { width: 1200px; height: 880px; overflow: hidden; }
  body {
    background: var(--stage);
    font-family: "Montserrat", sans-serif;
    position: relative;
  }
  .card {
    position: absolute;
    width: 620px;
    height: 354px;
    border-radius: 22px;
    overflow: hidden;
  }
  .card-front {
    left: 80px; top: 70px;
    background: var(--brand-blue);
  }
  .map-area {
    position: absolute;
    left: 60px; top: 40px;
    width: 500px; height: 270px;
    border-radius: 40px;
    background: radial-gradient(ellipse at center, var(--brand-blue-soft) 0%, var(--brand-blue) 75%);
  }
  .front-brand {
    position: absolute;
    left: 50%; top: 50%;
    transform: translate(-50%, -50%);
    display: flex; align-items: center; gap: 18px;
  }
  .front-mark {
    width: 74px; height: 74px;
    border: 4px solid var(--card-white);
    border-radius: 50%;
  }
  .front-name {
    color: var(--card-white);
    font-weight: 800;
    font-size: 58px;
    letter-spacing: 1px;
  }
  .card-back {
    left: 500px; top: 466px;
    background: var(--card-white);
  }
  .back-mark {
    position: absolute;
    right: -40px; top: -40px;
    width: 300px; height: 300px;
    border-radius: 50%;
    background: var(--tint);
    box-shadow: 0 0 0 10px var(--card-white), 0 0 0 20px var(--tint);
  }
  .back-info {
    position: absolute;
    left: 48px; bottom: 52px;
    color: var(--brand-blue);
  }
  .back-name {
    font-weight: 800;
    font-size: 46px;
    margin-bottom: 18px;
  }
  .person { font-weight: 700; font-size: 18px; line-height: 1.1; }
  .role { font-weight: 400; font-size: 16px; margin-bottom: 14px; }
  .contact {
    display: flex; align-items: center; gap: 8px;
    font-size: 15px; font-weight: 500; margin-top: 6px;
  }
  .contact svg { width: 20px; height: 20px; flex: none; }
</style>
</head>
<body>
  <section class="card card-front">
    <div class="map-area" role="img" aria-label="Dotted world map pattern in light blue"></div>
    <div class="front-brand">
      <div class="front-mark"></div>
      <span class="front-name">Tarvel</span>
    </div>
  </section>

  <section class="card card-back">
    <div class="back-mark"></div>
    <div class="back-info">
      <div class="back-name">Tarvel</div>
      <div class="person">Omar Haddad</div>
      <div class="role">Founder</div>
      <div class="contact">
        <svg viewBox="0 0 20 20" aria-hidden="true">
          <circle cx="10" cy="10" r="9" fill="none" stroke="currentColor" stroke-width="1.5"/>
          <path d="M7 5.5l2 2-1.2 1.4a6 6 0 0 0 3.3 3.3l1.4-1.2 2 2-1.3 1.5c-3.6-.4-6.9-3.7-7.3-7.3z" fill="currentColor"/>
        </svg>
        <span>(555) 014-2278</span>
      </div>
      <div class="contact">
        <svg viewBox="0 0 20 20" aria-hidden="true">
          <circle cx="10" cy="10" r="9" fill="none" stroke="currentColor" stroke-width="1.5"/>
          <rect x="5" y="6.5" width="10" height="7" rx="1" fill="currentColor"/>
          <path d="M5.5 7l4.5 3.5L14.5 7" fill="none" stroke="#fff" stroke-width="1"/>
        </svg>
        <span>hello@tarvelmail.com</span>
      </div>
    </div>
  </section>
</body>
</html>
```